Lantern Petals Website v.1 - attract floral shop franchisees

I need a simple information website for my new business. We are a franchisor of flower shops. The overall purpose of the website is to promote the company and the service, especially to potential franchisees and retailers. Only about 4 pages are required including homepage, About, For Supermarkets, For Franchisees, and Contact. No special functions are required except the site will have two separate inquiry forms that must be filled out online and submitted via automated email. Similarly, an email form should be linked from the Contact page. I have a logo and business cards designed by CraftHarbor, and I would like the site to have a consistent color scheme and style. The key to design will be to express the joy and love associated with flowers and floral bouquets.
IMPORTANT - I will be exporting the website design to Pageloft CMS in a site hosted by NetMarlow. For smooth integration into PageLoft hosted by NetMarlow, the designer should build the site using a PageLoft-friendly format. Ideally, they should use HTML, CSS, and PHP. Creating a custom theme or using a page builder that exports to PageLoft-compatible files is best. This ensures the site can be easily imported and managed within PageLoft.

Target Market(s)

Potential franchisees (existing florists or creative types who might like to own a floral business) and supermarkets who might want us to run their floral department

Industry/Entity Type

Floral retailing

Coding

Coded - Design and coding required

Number of Pages Required

4 page

Requirements
Must have
• A brand theme that is beautiful, consistent throughout and builds on the logo design
Nice to have
• Show gender and ethnic diversity in customers and florists. Pictures of happy florists (for franchisees) and pictures of amazing floral department displays (for supermarkets)

```html
<!DOCTYPE html>
<html lang="en">
<head>
<meta charset="utf-8">
<title>Lantern Petals</title>
<link href="https://fonts.googleapis.com/css2?family=Noto+Sans:wght@600;700&family=Montserrat:wght@400;500;600;700&family=Lora:wght@700&family=Allura&display=swap" rel="stylesheet">
<style>
:root{
  --green:#0b7535;
  --green-bright:#169944;
  --green-dark:#06220f;
  --orange:#f39c1f;
  --ink:#1b1b1b;
  --white:#ffffff;
  --navy:#0c1622;
}
*{margin:0;padding:0;box-sizing:border-box}
html,body{width:1200px;height:3976px;overflow:hidden}
body{position:relative;background:var(--white);font-family:"Montserrat",sans-serif;color:var(--ink)}
.abs{position:absolute}

/* hero */
.hero-photo{left:0;top:0;width:1200px;height:730px;background:linear-gradient(135deg,#bcb6ae 0%,#d9d4cc 35%,#8c2a2e 62%,#c63a3a 80%,#e9e4dc 100%)}
.nav{left:108px;top:15px;width:981px;height:119px;background:var(--green-dark);border:4px solid var(--orange);border-radius:60px;display:flex;align-items:center;padding:0 40px}
.brand{display:flex;align-items:center;gap:12px;color:var(--orange);font-family:"Montserrat",sans-serif;font-weight:600;font-size:26px}
.brand-dot{width:18px;height:18px;border-radius:50%;background:var(--orange)}
.nav-links{display:flex;gap:20px;margin-left:auto;margin-right:40px;list-style:none;font-family:"Lora",serif;font-weight:700;font-size:20px;color:var(--white)}
.nav-links .active{color:var(--orange)}
.hero-title{left:113px;top:196px;width:400px;font-family:"Noto Sans",sans-serif;font-weight:700;font-size:37px;line-height:44px;color:var(--white)}
.btn{display:flex;align-items:center;justify-content:center;height:52px;background:var(--white);border:3px solid var(--green);border-top:6px solid var(--orange);font-family:"Noto Sans",sans-serif;font-weight:700;font-size:18px;color:var(--green-dark);letter-spacing:.3px}
.hero-btn{left:113px;top:540px;width:213px}

/* welcome */
.welcome-kicker{left:122px;top:770px;font-family:"Noto Sans",sans-serif;font-weight:700;font-size:40px;color:var(--ink)}
.script{font-family:"Allura",cursive;font-weight:400}
.welcome-script{left:117px;top:808px;font-size:80px;color:var(--green)}
.body-text{font-size:17px;line-height:27px;color:#222}
.welcome-p1{left:117px;top:903px;width:540px}
.welcome-p2{left:117px;top:1099px;width:540px}
.welcome-btn{left:117px;top:1240px;width:215px}
.hex-cluster{left:665px;top:780px;width:430px;height:420px}

/* supermarkets */
.band-green{left:0;top:1343px}
.section-title{width:1200px;text-align:center;font-family:"Noto Sans",sans-serif;font-weight:700;font-size:40px}
.sm-title{left:0;top:1450px;color:var(--white)}
.sm-script{left:0;top:1500px;width:1200px;text-align:center;font-size:84px;color:var(--white)}
.sm-art{left:116px;top:1644px;width:447px;height:533px;border-radius:50%;background:radial-gradient(circle,#2f8d4d 0%,#4aa35f 38%,var(--green) 52%,#c69a3a 60%,var(--green) 68%)}
.checklist{list-style:none}
.checklist li{display:flex;gap:18px;align-items:flex-start;font-size:18px;line-height:18px;letter-spacing:.4px}
.checklist svg{flex:none;width:26px;height:26px;margin-top:-2px}
.sm-list{left:645px;top:1652px;width:460px;color:var(--white)}
.sm-list li{margin-bottom:0}
.sm-btn{left:646px;top:2108px;width:212px}

/* franchisees */
.fr-title{left:0;top:2405px;color:var(--ink)}
.fr-script{left:0;top:2450px;width:1200px;text-align:center;font-size:84px;color:var(--green)}
.fr-intro{left:118px;top:2575px;width:964px;text-align:center;font-size:17px;line-height:27px}
.fr-list{left:113px;top:2797px;width:480px;color:var(--ink)}
.fr-btn{left:113px;top:3250px;width:414px}
.fr-photo{left:684px;top:2798px;width:403px;height:491px;border-radius:14px;box-shadow:0 0 0 1px #e2e2e2;background:#fff;padding:8px}
.fr-photo div{width:100%;height:100%;border-radius:10px;background:linear-gradient(160deg,#3e5a3a 0%,#a03a66 40%,#d7568a 55%,#8d6a4a 80%,#b89b78 100%)}

/* footer */
.footer-wave{left:0;top:3375px}
.footer-text{color:var(--white)}
.foot-brand{left:113px;top:3562px;font-weight:600;font-size:30px;color:var(--white);display:flex;align-items:center;gap:12px}
.foot-brand .brand-dot{background:var(--white)}
.foot-about{left:113px;top:3685px;width:250px;font-size:13px;line-height:20px}
.foot-follow{left:113px;top:3752px;font-size:17px;font-weight:600}
.socials{left:113px;top:3785px;display:flex;gap:10px}
.socials span{width:38px;height:38px;border-radius:50%;background:var(--white)}
.foot-head{font-size:17px;font-weight:600;color:var(--white)}
.foot-links{left:409px;top:3569px}
.foot-links ul{list-style:none;margin-top:18px}
.foot-links li{font-size:14px;margin-bottom:20px;color:var(--white)}
.foot-loc{left:589px;top:3569px;width:240px}
.foot-loc p{font-size:12.5px;line-height:20px;color:var(--white)}
.foot-loc .small-head{font-size:13px;font-weight:600;margin-top:16px}
.foot-loc .phone{font-size:18px;font-weight:700;margin-top:6px}
.foot-news{left:866px;top:3569px;width:240px}
.foot-news p{font-size:12.5px;line-height:17px;color:var(--white);margin-top:14px}
.news-input{margin-top:14px;width:213px;height:41px;background:var(--white);border:1px solid #ddd;font-size:12px;color:#999;padding:12px 10px}
.news-btn{margin-top:11px;width:213px;height:40px;background:var(--orange);color:var(--white);font-weight:700;font-size:15px;display:flex;align-items:center;justify-content:center}
.copy-bar{left:0;top:3868px;width:1200px;height:108px;background:var(--navy)}
.copy{left:0;top:3904px;width:1200px;text-align:center;color:var(--white);font-size:18px}
.copy b{color:var(--orange);font-weight:600}
.to-top{left:1045px;top:3899px;width:36px;height:36px;border-radius:50%;background:var(--white)}
</style>
</head>
<body>

<!-- hero -->
<div class="abs hero-photo" role="img" aria-label="Smiling florist on the phone behind a counter of red roses and fresh flowers"></div>
<svg class="abs" style="left:0;top:580px" width="1200" height="150" viewBox="0 0 1200 150">
  <path d="M0 95 C220 120 420 140 640 70 C840 10 1020 20 1200 70 L1200 150 L0 150 Z" fill="#f39c1f"/>
  <path d="M0 110 C240 135 440 150 660 88 C850 40 1020 45 1200 95 L1200 150 L0 150 Z" fill="#0b7535"/>
  <path d="M0 122 C250 148 450 160 670 104 C860 58 1030 62 1200 110 L1200 150 L0 150 Z" fill="#ffffff"/>
</svg>
<nav class="abs nav">
  <div class="brand"><span class="brand-dot"></span>Lantern Petals</div>
  <ul class="nav-links">
    <li class="active">Home</li><li>About Us</li><li>For Supermarkets</li><li>For Franchisees</li><li>Contact</li>
  </ul>
</nav>
<h1 class="abs hero-title">Fresh flowers convey beauty and love, and in our view should become something every person regularly enjoys.</h1>
<div class="abs btn hero-btn">LEARN MORE</div>

<!-- welcome -->
<h2 class="abs welcome-kicker">Welcome to</h2>
<div class="abs script welcome-script">Lantern Petals</div>
<p class="abs body-text welcome-p1">Fresh flowers convey beauty and love, and in our view should become something every person regularly enjoys. Lantern Petals is an entrepreneurial company created to make top quality fresh flowers and professionally-designed bouquets accessible to every consumer at affordable prices.</p>
<p class="abs body-text welcome-p2">Professional florists typically sell the finest quality stems, design the most beautiful bouquets and provide the finest customer service, but their costs – of floral products, retail spaces, labor and marketing – force them</p>
<div class="abs btn welcome-btn">LEARN MORE</div>
<svg class="abs hex-cluster" viewBox="0 0 430 420" role="img" aria-label="Honeycomb of flower shop photos: bouquets, roses, a florist and a greenhouse">
  <polygon points="215,145 275,180 275,250 215,285 155,250 155,180" fill="#ffffff"/>
  <text x="215" y="222" text-anchor="middle" font-family="Montserrat, sans-serif" font-weight="600" font-size="20" fill="#f39c1f">Lantern Petals</text>
  <polygon points="165,45 225,10 285,45 285,115 225,150 165,115" fill="#b5586e"/>
  <polygon points="25,120 85,85 145,120 145,190 85,225 25,190" fill="#b98a2a"/>
  <polygon points="290,120 350,85 410,120 410,190 350,225 290,190" fill="#9a6a58"/>
  <polygon points="10,260 70,225 130,260 130,330 70,365 10,330" fill="#5e6f56"/>
  <polygon points="270,265 330,230 390,265 390,335 330,370 270,335" fill="#a6395a"/>
  <polygon points="145,335 205,300 265,335 265,405 205,440 145,405" fill="#4f7a55"/>
</svg>

<!-- supermarkets -->
<svg class="abs band-green" width="1200" height="960" viewBox="0 0 1200 960">
  <path d="M0 45 C200 80 360 95 560 55 C800 5 1000 0 1200 30 L1200 870 C1000 820 820 850 600 900 C380 950 160 930 0 920 Z" fill="#0b7535"/>
</svg>
<h2 class="abs section-title sm-title">For Supermarkets</h2>
<div class="abs script sm-script">Opportunity for Supermarkets</div>
<div class="abs sm-art" role="img" aria-label="Illustration of a green tulip stem with leaves framed by a golden ring"></div>
<ul class="abs checklist sm-list">
  <li style="margin-bottom:29px"><svg viewBox="0 0 26 26"><rect x="2" y="4" width="18" height="18" fill="#fff"/><path d="M6 13 L11 18 L23 4" stroke="#f39c1f" stroke-width="3" fill="none"/></svg>Enhance floral revenue streams with efficient assortments and new offerings</li>
  <li style="margin-bottom:29px"><svg viewBox="0 0 26 26"><rect x="2" y="4" width="18" height="18" fill="#fff"/><path d="M6 13 L11 18 L23 4" stroke="#f39c1f" stroke-width="3" fill="none"/></svg>Reduce the costs of operating a floral department</li>
  <li style="margin-bottom:29px"><svg viewBox="0 0 26 26"><rect x="2" y="4" width="18" height="18" fill="#fff"/><path d="M6 13 L11 18 L23 4" stroke="#f39c1f" stroke-width="3" fill="none"/></svg>Improve the quality, useful life and merchandising of floral products</li>
  <li style="margin-bottom:29px"><svg viewBox="0 0 26 26"><rect x="2" y="4" width="18" height="18" fill="#fff"/><path d="M6 13 L11 18 L23 4" stroke="#f39c1f" stroke-width="3" fill="none"/></svg>Provide attentive customer service, including semi-custom bouquets, by professional florist staff</li>
  <li style="margin-bottom:29px"><svg viewBox="0 0 26 26"><rect x="2" y="4" width="18" height="18" fill="#fff"/><path d="M6 13 L11 18 L23 4" stroke="#f39c1f" stroke-width="3" fill="none"/></svg>Maintain a beautiful, fresh and well-stocked environment</li>
  <li style="margin-bottom:29px"><svg viewBox="0 0 26 26"><rect x="2" y="4" width="18" height="18" fill="#fff"/><path d="M6 13 L11 18 L23 4" stroke="#f39c1f" stroke-width="3" fill="none"/></svg>Increase sales and profits</li>
  <li><svg viewBox="0 0 26 26"><rect x="2" y="4" width="18" height="18" fill="#fff"/><path d="M6 13 L11 18 L23 4" stroke="#f39c1f" stroke-width="3" fill="none"/></svg>Enhance the entire customer shopping environment</li>
</ul>
<div class="abs btn sm-btn">LEARN MORE</div>

<!-- franchisees -->
<h2 class="abs section-title fr-title">For Franchisees</h2>
<div class="abs script fr-script">Opportunity for New Florist Franchisees</div>
<p class="abs fr-intro">Lantern Petals brings the best of professional florists and supermarkets together for the benefit of consumers.&nbsp; It supports a national network of owner-operator franchisees, who in many cases are multi-site professional florists, with comprehensive services to enhance franchise profitability.&nbsp; Lantern Petals works with some of the country’s largest and most progressive supermarkets to provide franchisee ownership and operation of their strategically important floral departments.</p>
<ul class="abs checklist fr-list">
  <li style="margin-bottom:32px"><svg viewBox="0 0 26 26"><rect x="2" y="4" width="18" height="18" fill="#fff" stroke="#0b7535" stroke-width="2"/><path d="M6 13 L11 18 L23 4" stroke="#f39c1f" stroke-width="3" fill="none"/></svg>Be an owner, and your own boss</li>
  <li style="margin-bottom:32px"><svg viewBox="0 0 26 26"><rect x="2" y="4" width="18" height="18" fill="#fff" stroke="#0b7535" stroke-width="2"/><path d="M6 13 L11 18 L23 4" stroke="#f39c1f" stroke-width="3" fill="none"/></svg>Attractive earnings potential; paid weekly</li>
  <li style="margin-bottom:32px"><svg viewBox="0 0 26 26"><rect x="2" y="4" width="18" height="18" fill="#fff" stroke="#0b7535" stroke-width="2"/><path d="M6 13 L11 18 L23 4" stroke="#f39c1f" stroke-width="3" fill="none"/></svg>No experience necessary, we set you up to operate and provide extensive support</li>
  <li style="margin-bottom:32px"><svg viewBox="0 0 26 26"><rect x="2" y="4" width="18" height="18" fill="#fff" stroke="#0b7535" stroke-width="2"/><path d="M6 13 L11 18 L23 4" stroke="#f39c1f" stroke-width="3" fill="none"/></svg>Professional training provided, and a path to floral design industry certification</li>
  <li style="margin-bottom:32px"><svg viewBox="0 0 26 26"><rect x="2" y="4" width="18" height="18" fill="#fff" stroke="#0b7535" stroke-width="2"/><path d="M6 13 L11 18 L23 4" stroke="#f39c1f" stroke-width="3" fill="none"/></svg>Low operating and supply costs which leverage supermarket economies</li>
  <li style="margin-bottom:32px"><svg viewBox="0 0 26 26"><rect x="2" y="4" width="18" height="18" fill="#fff" stroke="#0b7535" stroke-width="2"/><path d="M6 13 L11 18 L23 4" stroke="#f39c1f" stroke-width="3" fill="none"/></svg>Affordable franchise fees and low initial investment</li>
  <li><svg viewBox="0 0 26 26"><rect x="2" y="4" width="18" height="18" fill="#fff" stroke="#0b7535" stroke-width="2"/><path d="M6 13 L11 18 L23 4" stroke="#f39c1f" stroke-width="3" fill="none"/></svg>Opportunities to expand to different locations</li>
</ul>
<div class="abs btn fr-btn">NEW FLORIST FRANCHISE INQUIRY</div>
<div class="abs fr-photo"><div role="img" aria-label="Florist's hands arranging a pink and green bouquet on a wooden table"></div></div>

<!-- footer -->
<svg class="abs footer-wave" width="1200" height="500" viewBox="0 0 1200 500">
  <path d="M0 20 C200 70 380 95 620 55 C860 10 1040 0 1200 15 L1200 500 L0 500 Z" fill="#f39c1f"/>
  <path d="M0 60 C220 105 400 125 640 85 C860 45 1040 40 1200 55 L1200 500 L0 500 Z" fill="#169944"/>
</svg>
<div class="abs foot-brand"><span class="brand-dot"></span>Lantern Petals</div>
<p class="abs footer-text foot-about">Lorem ipsum is are many var-iations of pass lacin of majority.Lorem ipsum is are many</p>
<div class="abs footer-text foot-follow">Follow us on</div>
<div class="abs socials"><span></span><span></span><span></span></div>
<div class="abs foot-links">
  <div class="foot-head">Links</div>
  <ul><li>Home</li><li>About Us</li><li>For Supermarkets</li><li>For Franchisees</li><li>Contact</li></ul>
</div>
<div class="abs foot-loc">
  <div class="foot-head">Location</div>
  <p style="margin-top:14px">Marrow Lane 18, Ashford,<br>USA - 40219</p>
  <p class="small-head">Contact Us</p>
  <p style="margin-top:4px">hello@lanternpetals.example</p>
  <p class="phone">Local 312-555-0174</p>
</div>
<div class="abs foot-news">
  <div class="foot-head">Newsletter</div>
  <p>Subscribe to our newsletter for discounts and suffer in some form</p>
  <div class="news-input">Enter your email</div>
  <div class="news-btn">Subscribe Now</div>
</div>
<div class="abs copy-bar"></div>
<p class="abs copy">© Copyright 2024 by <b>Lantern Petals</b></p>
<svg class="abs to-top" viewBox="0 0 36 36"><circle cx="18" cy="18" r="18" fill="#fff"/><path d="M10 21 L18 13 L26 21" stroke="#0c1622" stroke-width="4" fill="none"/></svg>

</body>
</html>
```